Flooring Company Wordpress Design Using Elementor

We need a website design using elementor for a flooring company. I have attached a word document with the entire content for the site. I have sample websites www.pellingtonrenovatesutah.com and www.stonepathtilesdenver.com

The site needs to look alot better than the samples. Modern and professional is what we are looking for. 100 times better than the sample websites.

I have images to be used in the site but the file is to large to attached here.

```html
<!DOCTYPE html>
<html lang="en">
<head>
<meta charset="utf-8">
<title>Halvard Floors</title>
<link href="https://fonts.googleapis.com/css2?family=Roboto:wght@400;500;700&display=swap" rel="stylesheet">
<style>
:root{
  --brand:#ffb400;
  --ink:#1e1e1e;
  --text:#555;
  --white:#fff;
  --footer:#262626;
}
*{box-sizing:border-box;margin:0;padding:0}
html,body{width:1200px;height:3778px;overflow:hidden}
body{font-family:'Roboto',sans-serif;color:var(--ink);background:var(--white);position:relative}
.abs{position:absolute}
.topbar{top:0;left:0;width:1200px;height:30px;background:var(--brand);color:#fff;font-size:13px}
.topbar .welcome{left:66px;top:8px}
.topbar .social{right:64px;top:7px;display:flex;gap:10px}
.sq{display:inline-block;width:15px;height:15px;border:2px solid #fff;border-radius:2px}
.header{top:30px;left:0;width:1200px;height:123px;background:#fff}
.logo{display:flex;align-items:center;gap:12px}
.logo-mark{width:22px;height:22px;background:var(--brand)}
.logo-name{font-weight:700;font-size:30px;line-height:34px;color:var(--ink);letter-spacing:.5px}
.header .logo{left:88px;top:38px}
.nav{left:478px;top:52px;display:flex;gap:39px;font-size:15px;font-weight:500}
.nav .active{color:var(--brand)}
.hero{top:153px;left:0;width:1200px;height:616px;background:linear-gradient(180deg,#5a5048 0%,#3e3630 45%,#6a3a1c 80%,#4a2612 100%)}
.hero-text{left:165px;top:189px;width:870px;text-align:center;color:#fff;font-size:26px;font-weight:500;line-height:35px}
.btn{display:inline-flex;align-items:center;justify-content:center;font-weight:500;font-size:15px;text-transform:uppercase}
.btn-solid{background:var(--brand);color:#fff}
.btn-line{border:3px solid var(--brand);color:var(--brand)}
.hero .explore{left:400px;top:371px;width:131px;height:42px}
.hero .estimate{left:581px;top:371px;width:219px;height:42px}
.dots{left:553px;top:562px;display:flex;gap:14px}
.dots span{width:21px;height:7px;background:#fff}
.dots span:first-child{background:var(--brand)}
.features{top:769px;left:0;width:1200px;height:454px}
.feature{top:84px;width:300px;text-align:center}
.feature h3{color:var(--brand);font-size:20px;font-weight:500;line-height:26px;margin-bottom:24px}
.feature p{font-size:13.5px;line-height:21.2px;color:var(--text)}
.partner{top:1223px;left:0;width:1200px;height:417px;background:linear-gradient(90deg,#2c2c2c,#3d4046 55%,#55514c)}
.partner-title{left:66px;top:68px;color:var(--brand);font-size:35px;font-weight:700}
.partner-copy{left:66px;top:129px;width:560px;color:#fff;font-size:13.5px;line-height:22.8px}
.partner .learn{left:66px;top:298px;width:131px;height:43px;border:3px solid var(--brand);color:#fff}
.card{top:52px;width:225px;height:274px;background:#fff;overflow:hidden}
.card-photo{width:225px;height:220px;background:linear-gradient(180deg,#f6f6f6 0%,#dcdde0 55%,#27324a 100%)}
.card-name{width:225px;color:var(--brand);font-size:16px;font-weight:500;text-align:center;margin-top:10px}
.card-role{width:225px;font-size:13.5px;color:#555;text-align:center;margin-top:4px}
.card-icons{left:56px;top:172px;display:flex;gap:10px}
.card-icons span{width:16px;height:16px;background:var(--brand);border-radius:2px}
.pdots{left:869px;top:355px;display:flex;gap:9px}
.pdots span{width:12px;height:12px;border-radius:50%;background:#fff}
.pdots span:first-child{background:var(--brand)}
.section-title{width:1200px;left:0;text-align:center;color:var(--brand);font-weight:700;font-size:35px;line-height:43px}
.grid{top:1841px;left:66px;width:1068px;height:645px;display:grid;grid-template-columns:repeat(3,356px);grid-template-rows:repeat(2,322.5px)}
.tile-a{background:linear-gradient(135deg,#dfe2e6,#8a8f96)}
.tile-b{background:linear-gradient(135deg,#f2f2f2,#7d8fa8)}
.tile-c{background:linear-gradient(135deg,#efe9e2,#b3a796)}
.tile-d{background:linear-gradient(135deg,#c8c1b6,#8a8070)}
.tile-e{background:linear-gradient(135deg,#eef0f2,#a46a3c)}
.feature-tile{background:var(--brand);padding:12px}
.feature-tile .inner{border:4px solid #fff;height:100%;text-align:center;color:#fff;padding:20px 18px}
.feature-tile h3{font-size:22px;font-weight:500;margin-bottom:18px}
.feature-tile p{font-size:13.5px;line-height:21px;margin-bottom:18px}
.feature-tile .more{font-weight:700;font-size:14px}
.viewall{left:534px;top:2551px;width:132px;height:43px}
.process{top:2741px;left:0;width:1200px}
.line{top:64px;left:188px;width:820px;height:6px;background:var(--brand)}
.step{width:260px;text-align:center}
.circle{width:134px;height:134px;border-radius:50%;margin:0 auto;background:#fff;border:4px solid #f2f2f2;display:flex;align-items:center;justify-content:center}
.circle.on{background:var(--brand);border-color:var(--brand)}
.step h4{font-size:16px;font-weight:500;line-height:21px;height:42px;display:flex;align-items:flex-end;justify-content:center;margin-top:24px}
.step p{margin-top:20px;font-size:13.5px;line-height:21.2px;color:var(--text)}
.cta{top:3129px;left:0;width:1200px;height:292px;background:var(--brand)}
.cta-title{width:1200px;text-align:center;top:45px;color:#fff;font-size:35px;font-weight:700}
.cta-label{left:76px;color:#fff;font-size:20px;font-weight:500}
.field{height:43px;background:#fff;font-size:13.5px;color:#777;padding:0 14px;display:flex;align-items:center;justify-content:space-between}
.cta .submit{left:947px;top:155px;width:176px;height:57px;background:#fff;color:var(--brand);font-size:16px}
.footer{top:3421px;left:0;width:1200px;height:357px;background:var(--footer);color:#fff}
.footer .logo{left:88px;top:56px}
.footer .logo-name{color:#fff}
.tagline{left:88px;top:160px;width:250px;text-align:center;font-size:13.5px;line-height:21px}
.fcol{top:48px}
.fcol h5{color:var(--brand);font-size:16px;font-weight:700;margin-bottom:18px}
.fcol li{list-style:none;font-size:13.5px;line-height:33.6px}
.hours td{font-size:13.5px;padding:0 18px 15px 0}
.fsocial{left:566px;top:215px;display:flex;gap:12px}
.fsocial span{width:30px;height:30px;background:var(--brand);border-radius:3px}
.rule{left:88px;top:3711px;width:1024px;height:1px;background:#555}
.copy{top:3740px;left:0;width:1200px;text-align:center;color:#fff;font-size:15px;font-weight:500}
.copy b{color:var(--brand);font-weight:500}
</style>
</head>
<body>

<div class="abs topbar">
  <span class="abs welcome">Welcome Our Website</span>
  <div class="abs social"><span class="sq"></span><span class="sq"></span><span class="sq"></span><span class="sq"></span><span class="sq"></span></div>
</div>

<header class="abs header">
  <div class="abs logo"><span class="logo-mark"></span><span class="logo-name">HALVARD<br>FLOORS</span></div>
  <nav class="abs nav"><span class="active">HOME</span><span>ABOUT US</span><span>SERVICES</span><span>FAQ</span><span>PROJECTS</span><span>CONTACT US</span></nav>
</header>

<section class="abs hero" role="img" aria-label="Modern living room with white sofa and polished hardwood floor">
  <p class="abs hero-text">Are you tired of having your residential or commercial floors messed up by unprofessional services? Allow Halvard Floors to change your floor installation and removal story today with our premium services, creativity, and personalized approach.</p>
  <span class="abs btn btn-solid explore">Explore</span>
  <span class="abs btn btn-line estimate">Get your free estimate</span>
  <div class="abs dots"><span></span><span></span><span></span></div>
</section>

<section class="abs features">
  <div class="abs feature" style="left:102px">
    <h3>MINIMAL STRESS STRESS<br>ON YOUR PLATE</h3>
    <p>Floor installation or removal can be stressful for both parties. You have to relocate most of your property on the affected area to a new location and adjust your daily operation. The last thing we want to do is add to that. Hence, we take a proactive, customer-focused approach on all our floor installation. We will assist you with your property relocation and covering and ensure a quick and smooth process.</p>
  </div>
  <div class="abs feature" style="left:440px">
    <h3>A FLOOR WORTHY OF<br>YOUR HOME</h3>
    <p>The quality and type of your floor are as important as its style and appeal. The wrong combination could see you spending a lot on maintenance and feeling frustrated. That's why here at Halvard Floors, don't just go with what is available, but what fits best. We will work with you to identify the kind of floor that matches your lifestyle, theme, preference, and strikes a balance between lower maintenance and durability.</p>
  </div>
  <div class="abs feature" style="left:779px;width:314px">
    <h3>QUALIFIED AND<br>CERTIFIED EXPERTS</h3>
    <p>After spending a lot to finally get that property of your dream, the last thing you want is some rookie messing it up and getting you back on your plans. Here at Halvard Floors, we understand this and strive to avoid its occurrence. Hence, we never assign your projects to unvetted professionals. Our team of experts is made up of only highly experienced and passionate individuals licensed in their specific fields to ensure the best results possible.</p>
  </div>
</section>

<section class="abs partner" role="img" aria-label="Installer kneeling on a carpeted floor">
  <h2 class="abs partner-title">A RELIABLE PARTNER TO LEAN ON</h2>
  <p class="abs partner-copy">Halvard Floors comes with over 14 years of experience in floor installation. We are specialists when it comes to tile installation, hardwood installation, carpet installation, tile backsplash installation, vinyl installation, laminate floor installation, and floor removal. Over the years, we have come to position ourselves as the professional hands our customers need for all their installation and removal needs. With us, you can be assured of on-time performance, professional services, and prime craftsmanship.</p>
  <span class="abs btn learn">Learn more</span>
  <div class="abs card" style="left:656px">
    <div class="card-photo" role="img" aria-label="Portrait of the chief designer in a dark suit"></div>
    <div class="abs card-icons"><span></span><span></span><span></span><span></span></div>
    <div class="card-name">LUCAS VERNE</div>
    <div class="card-role">CHIEF DESIGNER</div>
  </div>
  <div class="abs card" style="left:893px">
    <div class="card-photo" role="img" aria-label="Portrait of the flooring expert in a navy blazer"></div>
    <div class="card-name">MIRA CASTELL</div>
    <div class="card-role">FLOORING EXPERT</div>
  </div>
  <div class="abs pdots"><span></span><span></span></div>
</section>

<h2 class="abs section-title" style="top:1722px">MAKE YOUR FLOORS SCREAM<br>QUALITY AND BEAUTY</h2>

<div class="abs grid">
  <div class="tile-a" role="img" aria-label="Two workers cutting floor tiles"></div>
  <div class="feature-tile"><div class="inner">
    <h3>HARDWOOD INSTALLATION</h3>
    <p>Are you looking for the best hardwood installers near you? You are at the right place. Halvard Floors is an expert in all kinds of hardwood installation, from solid to engineered hardwood. We will guide you toward choosing the right wood for your home or business to ensure your space is fixed with the best match.</p>
    <span class="more">LEARN MORE &raquo;</span>
  </div></div>
  <div class="tile-b" role="img" aria-label="Installer laying laminate planks with a mallet"></div>
  <div class="tile-c" role="img" aria-label="Measuring carpet with a tape measure"></div>
  <div class="tile-d" role="img" aria-label="Hands fitting vinyl floor planks"></div>
  <div class="tile-e" role="img" aria-label="Worker removing old floorboards with a hammer"></div>
</div>

<span class="abs btn btn-solid viewall">View all</span>

<h2 class="abs section-title" style="top:2672px">A SIMPLE, REPEATABLE PROCESS</h2>

<section class="abs process">
  <div class="abs line"></div>
  <div class="abs step" style="left:58px">
    <div class="circle on"><svg width="70" height="70" viewBox="0 0 70 70" fill="none" stroke="#fff" stroke-width="4"><rect x="10" y="16" width="50" height="44" rx="3"/><line x1="10" y1="28" x2="60" y2="28"/><line x1="22" y1="8" x2="22" y2="20"/><line x1="48" y1="8" x2="48" y2="20"/><g fill="#fff" stroke="none"><rect x="18" y="36" width="7" height="6"/><rect x="31" y="36" width="7" height="6"/><rect x="44" y="36" width="7" height="6"/><rect x="18" y="47" width="7" height="6"/><rect x="31" y="47" width="7" height="6"/></g></svg></div>
    <h4>SCHEDULE AN<br>APPOINTMENT</h4>
    <p>Fill out the form on our site or call us on our hotline to relay your needs and schedule a free site inspection. It is that simple!</p>
  </div>
  <div class="abs step" style="left:326px">
    <div class="circle"><svg width="64" height="70" viewBox="0 0 64 70" fill="none" stroke="#ffb400" stroke-width="4"><path d="M32 4 L58 14 V34 C58 50 46 60 32 66 C18 60 6 50 6 34 V14 Z"/><path d="M16 26 H48 M16 36 H48 M20 46 H44"/></svg></div>
    <h4>YOUR PREFERRED<br>FLOOR MATERIAL</h4>
    <p>Based on our findings on consultation and our inspection, we will help you figure out the right type of floor for your home or business space.</p>
  </div>
  <div class="abs step" style="left:603px">
    <div class="circle"><svg width="80" height="70" viewBox="0 0 80 70"><rect x="18" y="8" width="44" height="34" fill="#ffb400"/><path d="M26 8v34M36 8v34M46 8v34M54 8v34M18 20h44M18 31h44" stroke="#fff" stroke-width="2"/><path d="M14 48 H66 L76 64 H4 Z" fill="#ffb400"/></svg></div>
    <h4>PREMIUM INSTALLATION</h4>
    <p>After the two stages are done, and you have approved the work date, our professionals for your floor will begin work on your property.</p>
  </div>
  <div class="abs step" style="left:878px">
    <div class="circle"><svg width="70" height="70" viewBox="0 0 70 70" fill="none" stroke="#ffb400" stroke-width="5"><circle cx="35" cy="35" r="30"/><circle cx="25" cy="28" r="3" fill="#ffb400"/><circle cx="45" cy="28" r="3" fill="#ffb400"/><path d="M21 43 C27 52 43 52 49 43"/></svg></div>
    <h4>A HAPPY YOU!</h4>
    <p>With a quality job done, go ahead and enjoy your floors for years to come with minimal maintenance on your side!</p>
  </div>
</section>

<section class="abs cta">
  <h2 class="abs cta-title">GET STARTED NOW</h2>
  <span class="abs cta-label" style="top:146px">APPOINTMENT</span>
  <span class="abs cta-label" style="top:215px">YOUR INFO</span>
  <div class="abs field" style="left:252px;top:127px;width:211px">Type of appointment</div>
  <div class="abs field" style="left:475px;top:127px;width:211px">Closest city <span>&#8964;</span></div>
  <div class="abs field" style="left:698px;top:127px;width:211px">Date <span>&#9638;</span></div>
  <div class="abs field" style="left:252px;top:197px;width:211px">Name</div>
  <div class="abs field" style="left:475px;top:197px;width:211px">Contact</div>
  <div class="abs field" style="left:698px;top:197px;width:211px">Address</div>
  <span class="abs btn submit">Submit</span>
</section>

<footer class="abs footer">
  <div class="abs logo"><span class="logo-mark"></span><span class="logo-name">HALVARD<br>FLOORS</span></div>
  <p class="abs tagline">CREATING BEAUTIFUL MEMORIES AND MAGNIFICENT FLOORS SINCE 2006 HERE IN FLORIDA</p>
  <div class="abs fcol" style="left:413px"><h5>QUICK LINKS</h5><ul><li>HOME</li><li>ABOUT US</li><li>SERVICES</li><li>FAQ</li><li>PROJECTS</li><li>CONTACT US</li></ul></div>
  <div class="abs fcol" style="left:566px"><h5>OFFICE HOURS</h5>
    <table class="hours"><tr><td>MON-FRI</td><td>9:00 AM - 6:00 PM</td></tr><tr><td>SAT</td><td>10:00 AM - 6:00 PM</td></tr><tr><td>SUN</td><td>CLOSED</td></tr></table>
  </div>
  <div class="abs fsocial"><span></span><span></span><span></span><span></span><span></span></div>
  <div class="abs fcol" style="left:807px"><h5>CONTACT US</h5><ul><li>ORCHID 42 AVE.</li><li>32801, RIVERTON</li><li>FLORIDA,</li><li>USA</li><li>+1-407-555-0142</li></ul></div>
  <div class="abs fcol" style="left:980px"><h5>AREAS SERVED</h5><ul><li>ORLANDO, FL</li><li>WINDERMERE, FL</li><li>WINTER PARK, FL</li><li>WINTER GARDEN, FL</li><li>LAKE MARY, FL</li><li>LAKE NONA, FL</li></ul></div>
</footer>
<div class="abs rule"></div>
<p class="abs copy">Copyright &copy; <b>HALVARD FLOORS</b> All Rights Reserved.</p>

</body>
</html>
```